Amber Orchard (instructional dating book)

Title: Amber Orchard
Subtitle: Where to plant tulips along a crooked brick path
Author: R.K. Tolvane
I'm seeking the title to be central with the subtitle underneath and the author slightly lower and to the left. Perhaps a border or two around the font. I thought the background could look aged (off color and old textured paper) and the background slightly punched into the texture like a typewriter has been used. I imagine it something like an old Pemberworth playbook or 1940s morse code manual. Many thanks!

Target Market(s)

18 to 45 year old single people

Industry/Entity Type

Dating

Font styles to use
Serif

Requirements
Must have
• Text with border or two
Nice to have
• Traditional feel. The book is instructional.
Should not have
• Too much color or flair

```html
<!DOCTYPE html>
<html lang="en">
<head>
<meta charset="utf-8">
<title>Amber Orchard — R.K. Tolvane</title>
<link rel="stylesheet" href="https://fonts.googleapis.com/css2?family=Special+Elite&family=Courier+Prime:wght@700&display=swap">
<style>
  :root {
    --paper-light: #e4d6b6;
    --paper-mid: #d2bf99;
    --paper-dark: #a88d62;
    --stain: rgba(110, 78, 40, 0.28);
    --ink: #3b2414;
    --ink-soft: #2a1d14;
    --machine-mid: rgba(120, 98, 70, 0.55);
    --machine-dark: #4a3a2a;
  }
  html, body {
    margin: 0;
    padding: 0;
    overflow: hidden;
    background: var(--paper-mid);
  }
  .cover {
    position: relative;
    width: 804px;
    height: 1200px;
    overflow: hidden;
    background:
      radial-gradient(ellipse 32% 26% at 92% 94%, var(--stain), transparent 70%),
      radial-gradient(ellipse 28% 18% at 18% 12%, rgba(130, 100, 60, 0.18), transparent 70%),
      radial-gradient(ellipse 30% 22% at 72% 38%, rgba(140, 110, 70, 0.14), transparent 70%),
      radial-gradient(ellipse 80% 70% at 50% 45%, var(--paper-light), var(--paper-mid) 60%, var(--paper-dark) 100%);
  }
  .paper-texture {
    position: absolute;
    inset: 0;
    width: 804px;
    height: 1200px;
    pointer-events: none;
  }
  .title-frame {
    position: absolute;
    left: 97px;
    top: 290px;
    width: 622px;
    height: 191px;
    border: 2px solid var(--ink-soft);
    box-sizing: border-box;
    text-align: center;
  }
  .title {
    margin: 30px 0 0;
    font-family: "Special Elite", "Courier New", monospace;
    font-weight: 400;
    font-size: 66px;
    letter-spacing: 2px;
    line-height: 1;
    color: var(--ink);
  }
  .subtitle {
    margin: 26px 0 0;
    font-family: "Courier Prime", "Courier New", monospace;
    font-weight: 700;
    font-size: 18px;
    line-height: 1;
    color: var(--ink-soft);
  }
  .typewriter-art {
    position: absolute;
    left: 170px;
    top: 540px;
    width: 456px;
    height: 420px;
    border-radius: 30px 30px 18px 18px;
    background:
      linear-gradient(to bottom,
        rgba(200, 182, 150, 0) 0%,
        rgba(150, 128, 96, 0.25) 30%,
        var(--machine-mid) 65%,
        rgba(120, 98, 70, 0.55) 88%,
        var(--machine-dark) 94%,
        var(--machine-dark) 100%);
  }
  .author {
    position: absolute;
    left: 75px;
    top: 1100px;
    margin: 0;
    font-family: "Courier Prime", "Courier New", monospace;
    font-weight: 700;
    font-size: 26px;
    color: var(--ink-soft);
  }
</style>
</head>
<body>
  <main class="cover">
    <svg class="paper-texture" viewBox="0 0 804 1200" aria-hidden="true">
      <filter id="mottle" x="0" y="0" width="100%" height="100%">
        <feTurbulence type="fractalNoise" baseFrequency="0.012 0.018" numOctaves="5" seed="7"/>
        <feColorMatrix type="matrix" values="0 0 0 0 0.42  0 0 0 0 0.30  0 0 0 0 0.16  0 0 0 -1.6 0.95"/>
      </filter>
      <filter id="grain" x="0" y="0" width="100%" height="100%">
        <feTurbulence type="fractalNoise" baseFrequency="0.9" numOctaves="2" seed="3"/>
        <feColorMatrix type="matrix" values="0 0 0 0 0.30  0 0 0 0 0.22  0 0 0 0 0.12  0 0 0 -1.2 0.75"/>
      </filter>
      <rect width="804" height="1200" filter="url(#mottle)" opacity="0.55"/>
      <rect width="804" height="1200" filter="url(#grain)" opacity="0.35"/>
    </svg>
    <header class="title-frame">
      <h1 class="title">Amber Orchard</h1>
      <p class="subtitle">Where to plant tulips along a crooked brick path</p>
    </header>
    <div class="typewriter-art" role="img" aria-label="Sepia photograph of a vintage typewriter fading into the paper"></div>
    <p class="author">R.K. Tolvane</p>
  </main>
</body>
</html>
```